Create professional business cards using the attached logo previously designed using PixelForge. Would like to see a business card that stands out from the crowd.

One side should just have our logo and our business name ie Roadlamp Consulting Partners, and the other side should have a smaller version of logo and company name, but together with our business details detailed below. Two cards will need to be produced for myself and my business partner

Target Market(s)

Professional financial advice to streetlighting engineers and finance people.

Industry/Entity Type

Business

Contact Information for Business Card

The business card will need to contain; name, title (ie Director, email, mobile number, and website address.

Font styles to use
Other font styles liked:
• HoratioB and HoratioM

Requirements
Must have
• We would like modern clean looking professional business cards that incorprates the attached .ai file logo. Font used is HoratioB and HoratioM and the name of the company is Roadlamp Consulting Partners.
• One side should just have our logo and our business name ie Roadlamp Consulting Partners, and the other side should have a smaller version of logo and company name, but together with our business details as above.
Nice to have
• We would potentially like to emboss the logo and name Roadlamp Consulting Partners Ltd. Perhaps something that reflects the transition from night to day eg white on one side, black on the other.
Should not have
• We are open minded. Do not want anything that would appear as a stock copy and paste from a 'normal' business card website eg CardMilo

```html
<!DOCTYPE html>
<html lang="en">
<head>
<meta charset="utf-8">
<title>Roadlamp Consulting Partners – Business Cards</title>
<link href="https://fonts.googleapis.com/css2?family=Jost:wght@400;500;600&display=swap" rel="stylesheet">
<style>
  :root {
    --backdrop: #d0d1d3;
    --card-night: #000000;
    --card-day: #ffffff;
    --ink-light: #ffffff;
    --ink-dark: #111111;
    --rim-grey: #8c8d90;
    --accent-blue: #1fa3d6;
    --accent-violet: #5b3a96;
    --accent-pink: #ec1d7a;
    --accent-red: #f0523c;
    --accent-orange: #f7a21b;
    --accent-yellow: #f4ea2a;
    --accent-green: #7cc242;
    --shadow: rgba(0,0,0,0.35);
  }
  * { margin: 0; padding: 0; box-sizing: border-box; }
  html, body {
    width: 1200px; height: 1000px; overflow: hidden;
    background: var(--backdrop);
    font-family: "Jost", "Century Gothic", sans-serif;
  }
  .card {
    position: absolute;
    left: 280px;
    width: 670px; height: 393px;
    overflow: hidden;
    box-shadow: 6px 6px 8px var(--shadow);
  }
  .card--front { top: 92px; background: var(--card-night); }
  .card--back { top: 516px; background: var(--card-day); }

  .card__bands, .card__feature {
    position: absolute; inset: 0; width: 670px; height: 393px;
  }

  .brand { position: absolute; display: flex; align-items: center; z-index: 1; }
  .brand__dot { border-radius: 50%; background: var(--accent-pink); flex: none; }
  .brand__name {
    font-weight: 600; text-transform: uppercase; line-height: 1.08;
    letter-spacing: 0.005em; white-space: nowrap;
  }
  .card--front .brand { left: 138px; top: 158px; }
  .card--front .brand__dot { width: 52px; height: 52px; margin-right: 27px; }
  .card--front .brand__name { color: var(--ink-light); font-size: 31px; }

  .card--back .brand { left: 33px; top: 44px; }
  .card--back .brand__dot { width: 44px; height: 44px; margin-right: 21px; }
  .card--back .brand__name { color: var(--ink-dark); font-size: 24px; }

  .person { position: absolute; left: 101px; top: 160px; color: var(--ink-dark); }
  .person__name { font-size: 35px; font-weight: 600; line-height: 1.1; }
  .person__title { font-size: 23px; font-weight: 500; line-height: 1.2; }

  .contacts {
    position: absolute; top: 308px; list-style: none;
    color: var(--ink-dark); font-size: 19px; font-weight: 400;
  }
  .contacts--phones { left: 98px; }
  .contacts--web { left: 356px; }
  .contacts li { display: flex; align-items: center; height: 27px; white-space: nowrap; }
  .contacts svg { width: 24px; height: 24px; margin-right: 14px; flex: none; }
</style>
</head>
<body>

<section class="card card--front" aria-label="Business card front">
  <svg class="card__bands" viewBox="0 0 670 393" aria-hidden="true">
    <defs>
      <linearGradient id="band-top" x1="566" y1="103" x2="670" y2="0" gradientUnits="userSpaceOnUse">
        <stop offset="0" stop-color="#1fa3d6"/>
        <stop offset="0.25" stop-color="#5b3a96"/>
        <stop offset="0.5" stop-color="#ec1d7a"/>
        <stop offset="0.68" stop-color="#f0523c"/>
        <stop offset="0.85" stop-color="#f4ea2a"/>
        <stop offset="1" stop-color="#7cc242"/>
      </linearGradient>
      <linearGradient id="band-bottom" x1="48" y1="345" x2="0" y2="393" gradientUnits="userSpaceOnUse">
        <stop offset="0" stop-color="#1fa3d6"/>
        <stop offset="0.3" stop-color="#5b3a96"/>
        <stop offset="0.6" stop-color="#ec1d7a"/>
        <stop offset="0.85" stop-color="#f7a21b"/>
        <stop offset="1" stop-color="#f4ea2a"/>
      </linearGradient>
    </defs>
    <polygon points="462,0 670,0 670,206" fill="url(#band-top)"/>
    <polygon points="0,296 0,393 96,393" fill="url(#band-bottom)"/>
  </svg>

  <div class="brand">
    <span class="brand__dot"></span>
    <p class="brand__name">Roadlamp<br>Consulting Partners</p>
  </div>
</section>

<section class="card card--back" aria-label="Business card back">
  <svg class="card__feature" viewBox="0 0 670 393" role="img" aria-label="Large colourful woven lightbulb artwork in violet, pink, blue and yellow tones">
    <defs>
      <linearGradient id="feature-glow" x1="430" y1="40" x2="670" y2="260" gradientUnits="userSpaceOnUse">
        <stop offset="0" stop-color="#2a1040"/>
        <stop offset="0.35" stop-color="#8a3a8e"/>
        <stop offset="0.6" stop-color="#c24a9a"/>
        <stop offset="0.85" stop-color="#5a6fb8"/>
        <stop offset="1" stop-color="#2a1a3a"/>
      </linearGradient>
    </defs>
    <path d="M450,0 C410,50 405,150 432,215 C455,262 520,285 590,290 C630,293 655,302 672,320 L672,-5 Z"
          fill="url(#feature-glow)" stroke="var(--rim-grey)" stroke-width="10"/>
  </svg>

  <div class="brand">
    <span class="brand__dot"></span>
    <p class="brand__name">Roadlamp<br>Consulting Partners</p>
  </div>

  <div class="person">
    <p class="person__name">Name</p>
    <p class="person__title">Title</p>
  </div>

  <ul class="contacts contacts--phones">
    <li>
      <svg viewBox="0 0 24 24" aria-hidden="true"><circle cx="12" cy="12" r="10.5" fill="none" stroke="#111" stroke-width="1.5"/><path d="M8.5 7.5l2 -0.5 1 2.5-1.3 1c.6 1.3 1.4 2.1 2.6 2.7l1-1.3 2.5 1-.5 2c-4 .3-7.6-3.3-7.3-7.4z" fill="none" stroke="#111" stroke-width="1.3" stroke-linejoin="round"/></svg>
      <span>123-456-7890</span>
    </li>
    <li>
      <svg viewBox="0 0 24 24" aria-hidden="true"><circle cx="12" cy="12" r="10.5" fill="none" stroke="#111" stroke-width="1.5"/><rect x="8.5" y="6" width="7" height="12" rx="1.2" fill="none" stroke="#111" stroke-width="1.4"/><line x1="10" y1="15.5" x2="14" y2="15.5" stroke="#111" stroke-width="1.2"/></svg>
      <span>123-546-7890</span>
    </li>
  </ul>

  <ul class="contacts contacts--web">
    <li>
      <svg viewBox="0 0 24 24" aria-hidden="true"><circle cx="12" cy="12" r="10.5" fill="none" stroke="#111" stroke-width="1.5"/><rect x="7" y="8.5" width="10" height="7" fill="none" stroke="#111" stroke-width="1.3"/><path d="M7 8.5l5 4 5-4" fill="none" stroke="#111" stroke-width="1.3"/></svg>
      <span>name@yourdomain.com</span>
    </li>
    <li>
      <svg viewBox="0 0 24 24" aria-hidden="true"><circle cx="12" cy="12" r="10.5" fill="none" stroke="#111" stroke-width="1.5"/><path d="M7 8.5l2 7 3-5.5 3 5.5 2-7" fill="none" stroke="#111" stroke-width="1.4" stroke-linejoin="round"/></svg>
      <span>www.yourdomain.com</span>
    </li>
  </ul>
</section>

</body>
</html>
```